Marketing Collateral for Construction Company
Keystone Cellar Craftworks
Attention Designers:
I have uploaded a number of pictures of basement project that our company has done. Please use these pictures where you think they will work in the designs for the marketing peripherals.
Thank you,
Mark
where is the content for the flyer and brochure?
@QW - please check your private messages on top right corner once you login to your account & reply. Thanks
Designers,
I have changed the scope of the project only to include:
-tri-fold brochure
-flyer
-door hanger
I have also uploaded AI files for you to use in your designs. Please let me know if you need more source files or a different format.
Thanks,

```html
<!DOCTYPE html>
<html lang="en">
<head>
<meta charset="utf-8">
<title>Keystone Cellar Craftworks – Marketing Collateral</title>
<link rel="stylesheet" href="https://fonts.googleapis.com/css2?family=Open+Sans:wght@400;600;700&family=Lato:ital,wght@0,400;0,700;1,400&display=swap">
<style>
:root{
  --green-deep:#1c6a2c;
  --green:#4f9a2a;
  --green-light:#8cc63f;
  --blue-deep:#173f7a;
  --blue:#1f5fae;
  --blue-light:#55a7dd;
  --ink:#3a3a3a;
  --paper:#ffffff;
  --canvas:#ffffff;
  --wood:#6b4a2b;
  --stone:#b59a7a;
}
*{box-sizing:border-box;margin:0;padding:0}
html,body{width:1200px;height:871px;overflow:hidden;background:var(--canvas)}
body{position:relative;font-family:"Open Sans",Arial,sans-serif;color:var(--ink)}
.piece{position:absolute;overflow:hidden;background:var(--paper);box-shadow:0 0 0 1px #e3e3e3}
.panel{position:absolute;top:0;bottom:0;overflow:hidden}
.swoosh{position:absolute;left:0;width:100%;display:block}
.body-text{font-size:5.6px;line-height:7.4px;color:var(--ink);text-align:left}
.section-bar{position:absolute;height:16px;background:linear-gradient(90deg,var(--blue-deep),var(--green));color:#fff;font:600 9px/16px "Open Sans",Arial,sans-serif;padding-left:10px;letter-spacing:.5px}
.brand{display:flex;align-items:center;gap:6px}
.brand-dot{width:22px;height:22px;border-radius:50%;background:var(--green);flex:none}
.brand-name{font:700 12px/1.1 "Open Sans",Arial,sans-serif;color:var(--blue-deep)}
.tagline{font:italic 400 13px "Lato",Arial,sans-serif;color:var(--green-deep);border-top:1px solid var(--green);padding-top:3px;margin-top:4px}
.photo{position:absolute}
.art-slot{position:absolute;background:linear-gradient(135deg,#cfe3ef,#9cc3de 60%,#b8d79a)}
.service-title{font:400 14px "Open Sans",Arial,sans-serif;color:var(--blue)}
.contact{font-size:6px;line-height:8px;color:var(--ink)}
.list{list-style:none;color:#fff;font:400 10px/14px "Lato",Arial,sans-serif}
.cols{display:flex;gap:10px}
.cols .body-text{flex:1}
</style>
</head>
<body>

<!-- Tri-fold brochure, outside -->
<section class="piece brochure-outside" style="left:0;top:0;width:480px;height:512px">
  <div class="panel" style="left:0;width:160px">
    <svg class="swoosh" style="top:0;height:150px" viewBox="0 0 160 150" preserveAspectRatio="none">
      <path d="M0 0H160V40C110 70 60 60 0 95Z" fill="var(--blue-deep)"/>
      <path d="M0 95C60 60 110 70 160 40V55C110 85 60 80 0 115Z" fill="var(--green)"/>
      <path d="M0 115C60 80 110 85 160 55V62C110 92 60 90 0 124Z" fill="var(--green-light)"/>
    </svg>
    <div class="art-slot" role="img" aria-label="Decorative illustration of a globe with a leaf sprout" style="left:6px;top:6px;width:64px;height:58px"></div>
    <div class="section-bar" style="left:0;top:192px;width:120px">about us</div>
    <p class="body-text" style="position:absolute;left:10px;top:216px;width:140px">Our crew plans and builds finished basements across the region, turning unused lower levels into bright living rooms, guest suites, home theaters and offices with careful detail, honest pricing and a schedule that respects your family and home. Our crew plans and builds finished basements across the region, turning unused lower levels into bright living rooms, guest suites, home theaters and offices with careful detail, honest pricing and a schedule that respects your family and home.</p>
    <p class="body-text" style="position:absolute;left:10px;top:300px;width:140px">Our crew plans and builds finished basements across the region, turning unused lower levels into bright living rooms, guest suites, home theaters and offices with careful detail, honest pricing and a schedule that respects your family and home.</p>
    <svg class="swoosh" style="bottom:0;height:90px" viewBox="0 0 160 90" preserveAspectRatio="none">
      <path d="M0 40C60 70 110 20 160 30V90H0Z" fill="var(--blue-deep)"/>
      <path d="M0 40C60 70 110 20 160 30V38C110 30 60 78 0 50Z" fill="var(--green)"/>
    </svg>
  </div>
  <div class="panel" style="left:160px;width:160px">
    <div class="photo" role="img" aria-label="Finished basement library with wooden bookshelves" style="left:0;top:0;width:160px;height:200px;background:linear-gradient(160deg,#3b2614,var(--wood) 50%,#caa775)"></div>
    <div class="brand" style="position:absolute;left:12px;top:214px;width:140px">
      <span class="brand-dot"></span><span class="brand-name">Keystone Cellar Craftworks</span>
    </div>
    <div class="tagline" style="position:absolute;left:12px;top:250px;width:136px">Form Following Function</div>
    <div class="brand" style="position:absolute;left:12px;top:350px;width:140px">
      <span class="brand-dot" style="width:16px;height:16px"></span><span class="brand-name" style="font-size:10px">Keystone Cellar Craftworks</span>
    </div>
    <p class="contact" style="position:absolute;left:12px;top:382px;width:140px">12 Quarry Lane, Suite 4<br>Phone: (555) 014-2290<br>Fax: (555) 014-2291<br>info@keystonecellar.example<br>www.keystonecellar.example</p>
  </div>
  <div class="panel" style="left:320px;width:160px;background:var(--green-deep)">
    <svg class="swoosh" style="top:0;height:512px" viewBox="0 0 160 512" preserveAspectRatio="none">
      <rect width="160" height="512" fill="var(--green-deep)"/>
      <path d="M0 0H160V250C100 300 50 280 0 320Z" fill="var(--paper)"/>
      <path d="M0 0H160V40C100 70 50 50 0 80Z" fill="var(--blue-deep)"/>
      <path d="M0 320C50 280 100 300 160 250V268C100 316 50 300 0 340Z" fill="var(--green-light)"/>
      <path d="M0 340C50 300 100 316 160 268V290C100 340 50 330 0 370Z" fill="var(--blue)"/>
    </svg>
    <div class="brand" style="position:absolute;left:12px;top:120px;width:140px">
      <span class="brand-dot"></span><span class="brand-name">Keystone Cellar Craftworks</span>
    </div>
    <div class="tagline" style="position:absolute;left:12px;top:158px;width:136px">Form Following Function</div>
    <ul class="list" style="position:absolute;left:60px;top:380px">
      <li>Special design</li><li>Interior design</li><li>Basement Additions</li><li>Outdoor Rooms</li>
    </ul>
  </div>
</section>

<!-- Flyer, top -->
<section class="piece flyer-top" style="left:504px;top:0;width:276px;height:500px">
  <svg class="swoosh" style="top:0;height:90px" viewBox="0 0 276 90" preserveAspectRatio="none">
    <path d="M0 0H276V30C180 70 90 40 0 70Z" fill="var(--blue-deep)"/>
    <path d="M0 70C90 40 180 70 276 30V42C180 82 90 56 0 82Z" fill="var(--green)"/>
  </svg>
  <div class="service-title" style="position:absolute;right:20px;top:90px">Our service</div>
  <div class="cols" style="position:absolute;left:14px;top:118px;width:248px">
    <p class="body-text">Our crew plans and builds finished basements across the region, turning unused lower levels into bright living rooms, guest suites, home theaters and offices with careful detail, honest pricing and a schedule that respects your family and home. Our crew plans and builds finished basements across the region, turning unused lower levels into bright living rooms, guest suites, home theaters and offices with careful detail, honest pricing and a schedule that respects your family and home.</p>
    <p class="body-text">Our crew plans and builds finished basements across the region, turning unused lower levels into bright living rooms, guest suites, home theaters and offices with careful detail, honest pricing and a schedule that respects your family and home. Our crew plans and builds finished basements across the region, turning unused lower levels into bright living rooms, guest suites, home theaters and offices with careful detail, honest pricing and a schedule that respects your family and home.</p>
  </div>
  <div class="photo" role="img" aria-label="Finished basement interior" style="left:14px;top:300px;width:70px;height:50px;background:linear-gradient(135deg,var(--stone),var(--wood))"></div>
  <div class="photo" role="img" aria-label="Basement family room" style="left:14px;top:356px;width:70px;height:50px;background:linear-gradient(135deg,#d8c6a5,#7a5a38)"></div>
  <svg class="swoosh" style="bottom:0;height:90px" viewBox="0 0 276 90" preserveAspectRatio="none">
    <path d="M0 40C90 80 180 20 276 40V90H0Z" fill="var(--green-deep)"/>
    <path d="M0 40C90 80 180 20 276 40V48C180 30 90 86 0 50Z" fill="var(--blue-light)"/>
  </svg>
  <div class="brand" style="position:absolute;right:14px;bottom:16px">
    <span class="brand-dot" style="width:14px;height:14px;background:#fff"></span><span class="brand-name" style="font-size:9px;color:#fff">Keystone Cellar Craftworks</span>
  </div>
</section>

<!-- Door hanger, front -->
<section class="piece door-front" style="left:800px;top:0;width:180px;height:410px">
  <svg class="swoosh" style="top:0;height:410px" viewBox="0 0 180 410" preserveAspectRatio="none">
    <path d="M0 0H180V110C120 150 60 120 0 160Z" fill="var(--blue-deep)"/>
    <path d="M0 160C60 120 120 150 180 110V124C120 164 60 136 0 174Z" fill="var(--green)"/>
    <path d="M0 330C60 360 120 300 180 320V410H0Z" fill="var(--green-deep)"/>
    <path d="M0 330C60 360 120 300 180 320V328C120 310 60 368 0 340Z" fill="var(--blue-light)"/>
    <rect x="88" y="0" width="4" height="30" fill="var(--paper)"/>
    <circle cx="90" cy="50" r="22" fill="var(--paper)"/>
  </svg>
  <div class="brand" style="position:absolute;left:14px;top:200px;width:150px">
    <span class="brand-dot"></span><span class="brand-name">Keystone Cellar Craftworks</span>
  </div>
  <div class="tagline" style="position:absolute;left:14px;top:240px;width:150px">Form Following Function</div>
</section>

<!-- Door hanger, back -->
<section class="piece door-back" style="left:1000px;top:0;width:195px;height:410px">
  <svg class="swoosh" style="top:0;height:410px" viewBox="0 0 195 410" preserveAspectRatio="none">
    <path d="M0 0H195V80C130 110 60 90 0 120Z" fill="var(--green-deep)"/>
    <path d="M0 120C60 90 130 110 195 80V92C130 122 60 104 0 132Z" fill="var(--blue-light)"/>
    <path d="M0 360C60 380 130 340 195 350V410H0Z" fill="var(--blue-deep)"/>
    <rect x="95" y="0" width="4" height="26" fill="var(--paper)"/>
    <circle cx="97" cy="46" r="22" fill="var(--paper)"/>
  </svg>
  <p class="body-text" style="position:absolute;left:14px;top:148px;width:167px">Our crew plans and builds finished basements across the region, turning unused lower levels into bright living rooms, guest suites, home theaters and offices with careful detail, honest pricing and a schedule that respects your family and home. Our crew plans and builds finished basements across the region, turning unused lower levels into bright living rooms, guest suites, home theaters and offices with careful detail, honest pricing and a schedule that respects your family and home. Our crew plans and builds finished basements across the region, turning unused lower levels into bright living rooms, guest suites, home theaters and offices with careful detail, honest pricing and a schedule that respects your family and home.</p>
</section>

<!-- Tri-fold brochure, inside -->
<section class="piece brochure-inside" style="left:0;top:525px;width:492px;height:346px">
  <div class="panel" style="left:0;width:164px">
    <svg class="swoosh" style="top:0;height:60px" viewBox="0 0 164 60" preserveAspectRatio="none">
      <path d="M0 0H164V20C110 40 50 30 0 45Z" fill="var(--blue-deep)"/>
      <path d="M0 45C50 30 110 40 164 20V28C110 48 50 40 0 54Z" fill="var(--green)"/>
    </svg>
    <div class="photo" role="img" aria-label="Finished basement bathroom with stone wall and vanity" style="left:0;top:60px;width:164px;height:220px;background:linear-gradient(150deg,#2a1d12,var(--wood) 45%,#e2cfae)"></div>
    <svg class="swoosh" style="bottom:0;height:66px" viewBox="0 0 164 66" preserveAspectRatio="none">
      <path d="M0 20C60 40 110 0 164 14V66H0Z" fill="var(--blue-deep)"/>
      <path d="M0 20C60 40 110 0 164 14V22C110 10 60 48 0 30Z" fill="var(--green)"/>
    </svg>
  </div>
  <div class="panel" style="left:164px;width:164px">
    <svg class="swoosh" style="top:0;height:50px" viewBox="0 0 164 50" preserveAspectRatio="none">
      <path d="M0 0H164V30C110 40 50 20 0 30Z" fill="var(--blue-deep)"/>
    </svg>
    <div class="section-bar" style="left:0;top:34px;width:120px">about us</div>
    <p class="body-text" style="position:absolute;left:10px;top:56px;width:146px">Our crew plans and builds finished basements across the region, turning unused lower levels into bright living rooms, guest suites, home theaters and offices with careful detail, honest pricing and a schedule that respects your family and home. Our crew plans and builds finished basements across the region, turning unused lower levels into bright living rooms, guest suites, home theaters and offices with careful detail, honest pricing and a schedule that respects your family and home.</p>
    <div class="section-bar" style="left:0;top:178px;width:120px">about us</div>
    <p class="body-text" style="position:absolute;left:10px;top:200px;width:146px">Our crew plans and builds finished basements across the region, turning unused lower levels into bright living rooms, guest suites, home theaters and offices with careful detail, honest pricing and a schedule that respects your family and home.</p>
    <svg class="swoosh" style="bottom:0;height:50px" viewBox="0 0 164 50" preserveAspectRatio="none">
      <path d="M0 20C60 40 110 0 164 14V50H0Z" fill="var(--green-deep)"/>
    </svg>
  </div>
  <div class="panel" style="left:328px;width:164px">
    <svg class="swoosh" style="top:0;height:50px" viewBox="0 0 164 50" preserveAspectRatio="none">
      <path d="M0 0H164V30C110 40 50 20 0 30Z" fill="var(--blue-deep)"/>
    </svg>
    <div class="section-bar" style="left:0;top:34px;width:120px">about us</div>
    <p class="body-text" style="position:absolute;left:10px;top:56px;width:146px">Our crew plans and builds finished basements across the region, turning unused lower levels into bright living rooms, guest suites, home theaters and offices with careful detail, honest pricing and a schedule that respects your family and home. Our crew plans and builds finished basements across the region, turning unused lower levels into bright living rooms, guest suites, home theaters and offices with careful detail, honest pricing and a schedule that respects your family and home. Our crew plans and builds finished basements across the region, turning unused lower levels into bright living rooms, guest suites, home theaters and offices with careful detail, honest pricing and a schedule that respects your family and home.</p>
    <svg class="swoosh" style="bottom:0;height:50px" viewBox="0 0 164 50" preserveAspectRatio="none">
      <path d="M0 20C60 40 110 0 164 14V50H0Z" fill="var(--green-deep)"/>
    </svg>
  </div>
</section>

<!-- Flyer, bottom middle -->
<section class="piece flyer-text" style="left:504px;top:525px;width:276px;height:346px">
  <svg class="swoosh" style="top:0;height:60px" viewBox="0 0 276 60" preserveAspectRatio="none">
    <path d="M0 0H276V20C180 50 90 24 0 44Z" fill="var(--green-deep)"/>
    <path d="M0 44C90 24 180 50 276 20V30C180 60 90 36 0 54Z" fill="var(--blue-light)"/>
  </svg>
  <p class="body-text" style="position:absolute;left:16px;top:70px;width:244px">Our crew plans and builds finished basements across the region, turning unused lower levels into bright living rooms, guest suites, home theaters and offices with careful detail, honest pricing and a schedule that respects your family and home. Our crew plans and builds finished basements across the region, turning unused lower levels into bright living rooms, guest suites, home theaters and offices with careful detail, honest pricing and a schedule that respects your family and home. Our crew plans and builds finished basements across the region, turning unused lower levels into bright living rooms, guest suites, home theaters and offices with careful detail, honest pricing and a schedule that respects your family and home.</p>
  <svg class="swoosh" style="bottom:0;height:60px" viewBox="0 0 276 60" preserveAspectRatio="none">
    <path d="M0 20C90 50 180 0 276 16V60H0Z" fill="var(--blue-deep)"/>
  </svg>
</section>

<!-- Flyer, bottom right -->
<section class="piece flyer-service" style="left:800px;top:525px;width:395px;height:346px">
  <svg class="swoosh" style="top:0;height:70px" viewBox="0 0 395 70" preserveAspectRatio="none">
    <path d="M0 0H395V24C260 60 130 30 0 54Z" fill="var(--blue-deep)"/>
    <path d="M0 54C130 30 260 60 395 24V34C260 70 130 44 0 64Z" fill="var(--green)"/>
  </svg>
  <div class="service-title" style="position:absolute;right:24px;top:74px">Our service</div>
  <p class="body-text" style="position:absolute;left:110px;top:98px;width:270px">Our crew plans and builds finished basements across the region, turning unused lower levels into bright living rooms, guest suites, home theaters and offices with careful detail, honest pricing and a schedule that respects your family and home. Our crew plans and builds finished basements across the region, turning unused lower levels into bright living rooms, guest suites, home theaters and offices with careful detail, honest pricing and a schedule that respects your family and home. Our crew plans and builds finished basements across the region, turning unused lower levels into bright living rooms, guest suites, home theaters and offices with careful detail, honest pricing and a schedule that respects your family and home.</p>
  <div class="photo" role="img" aria-label="Finished basement living space" style="left:16px;top:98px;width:84px;height:60px;background:linear-gradient(135deg,var(--stone),var(--wood))"></div>
  <svg class="swoosh" style="bottom:0;height:70px" viewBox="0 0 395 70" preserveAspectRatio="none">
    <path d="M0 24C130 60 260 10 395 26V70H0Z" fill="var(--green-deep)"/>
    <path d="M0 24C130 60 260 10 395 26V34C260 18 130 66 0 34Z" fill="var(--blue-light)"/>
  </svg>
  <div class="brand" style="position:absolute;right:16px;bottom:12px">
    <span class="brand-dot" style="width:14px;height:14px;background:#fff"></span><span class="brand-name" style="font-size:9px;color:#fff">Keystone Cellar Craftworks</span>
  </div>
</section>

</body>
</html>
```